Corvale Spine & Joint Business Card

Need a business card using the logo provided. I want brand side of the card to be grey with the logo in the center of the card in white.

On the other side I leave to the designers

Target Market(s)

Personal Injury Attorneys

Industry/Entity Type

Medical

Contact Information for Business Card

Name, CEO. Cell Phone, (Marlowe Teague, Address, Phone) (Homestead, Address, Phone) (Tallahassee, Address, Phone)

Colors

Designer to choose only greyscale colors for use in the design.

Requirements
Must have
• Logo by itself on one side

```html
<!DOCTYPE html>
<html lang="en">
<head>
<meta charset="utf-8">
<title>Corvale Spine &amp; Joint – Business Card</title>
<link href="https://fonts.googleapis.com/css2?family=Lato:wght@700&family=Nunito:wght@400;500&display=swap" rel="stylesheet">
<style>
  :root {
    --backdrop: #1c1c1c;
    --card-grey: #a5a5a7;
    --card-grey-light: #adadaf;
    --card-grey-dark: #9d9d9f;
    --paper: #ffffff;
    --ink: #1d1d1f;
    --muted: #9a9a9c;
    --rule: #a0a0a2;
  }
  * { margin: 0; padding: 0; box-sizing: border-box; }
  html, body { width: 1200px; height: 1200px; overflow: hidden; }
  body { background: var(--backdrop); position: relative; }

  .card {
    position: absolute;
    left: 260px;
    width: 684px;
    height: 443px;
    overflow: hidden;
  }

  /* Brand side */
  .card--front {
    top: 102px;
    background: linear-gradient(160deg, var(--card-grey-light), var(--card-grey-dark));
  }
  .brand-name {
    position: absolute;
    font-family: "Nunito", sans-serif;
    font-weight: 500;
    line-height: 1;
    white-space: nowrap;
  }
  .card--front .brand-name {
    left: 0; right: 0; top: 198px;
    text-align: center;
    font-size: 44px;
    letter-spacing: 1px;
    color: var(--paper);
  }

  /* Contact side */
  .card--back { top: 626px; background: var(--paper); }
  .side-strip { position: absolute; left: 0; width: 55px; background: var(--card-grey); }
  .side-strip--top { top: 0; height: 67px; }
  .side-strip--bottom { top: 119px; bottom: 0; }
  .name-bar {
    position: absolute; left: 266px; right: 0; top: 67px; height: 52px;
    background: linear-gradient(90deg, var(--card-grey-dark), var(--card-grey-light));
  }
  .person-name {
    position: absolute; left: 68px; top: 69px;
    font-family: "Lato", sans-serif; font-weight: 700;
    font-size: 26px; letter-spacing: 3px; color: var(--ink); line-height: 1;
    white-space: nowrap;
  }
  .person-role {
    position: absolute; left: 68px; top: 98px;
    font-family: "Nunito", sans-serif; font-size: 19px; color: var(--muted); line-height: 1;
  }

  .contact-icon { position: absolute; left: 13px; width: 36px; height: 36px; }
  .contact-text {
    position: absolute; left: 68px;
    font-family: "Nunito", sans-serif; font-weight: 500;
    font-size: 17px; line-height: 20px; color: var(--ink);
    white-space: nowrap;
  }
  .divider { position: absolute; left: 68px; width: 37px; height: 1.5px; background: var(--rule); }

  .card--back .brand-name {
    right: 52px; top: 330px;
    font-size: 24px;
    color: var(--muted);
  }
</style>
</head>
<body>

<section class="card card--front" aria-label="Brand side">
  <div class="brand-name">Corvale Spine &amp; Joint</div>
</section>

<section class="card card--back" aria-label="Contact side">
  <div class="side-strip side-strip--top"></div>
  <div class="side-strip side-strip--bottom"></div>
  <div class="name-bar"></div>

  <div class="person-name">MARLOWE T.</div>
  <div class="person-role">CEO</div>

  <svg class="contact-icon" style="top:179px" viewBox="0 0 36 36" aria-hidden="true">
    <circle cx="18" cy="18" r="18" fill="#fff"/>
    <path d="M9 18 L18 10 L27 18 H24 V26 H20 V21 H16 V26 H12 V18 Z" fill="#9a9a9c"/>
  </svg>
  <div class="contact-text" style="top:177px">Street Address Here<br>Singapore, 2222</div>
  <div class="divider" style="top:222px"></div>

  <svg class="contact-icon" style="top:232px" viewBox="0 0 36 36" aria-hidden="true">
    <circle cx="18" cy="18" r="18" fill="#fff"/>
    <rect x="9" y="12" width="18" height="12" fill="none" stroke="#9a9a9c" stroke-width="1.6"/>
    <path d="M9 12 L18 19 L27 12 M9 24 L15 18 M27 24 L21 18" fill="none" stroke="#9a9a9c" stroke-width="1.4"/>
  </svg>
  <div class="contact-text" style="top:240px">urname@email.com</div>
  <div class="divider" style="top:272px"></div>

  <svg class="contact-icon" style="top:286px" viewBox="0 0 36 36" aria-hidden="true">
    <circle cx="18" cy="18" r="18" fill="#fff"/>
    <path d="M9 15 Q18 8 27 15 L25 17 L22 15 V14 Q18 12 14 14 V15 L11 17 Z" fill="#9a9a9c"/>
    <rect x="11" y="18" width="14" height="8" rx="1.5" fill="#9a9a9c"/>
    <circle cx="18" cy="22" r="2" fill="#fff"/>
  </svg>
  <div class="contact-text" style="top:286px">+18 5520 3174 6092<br>+18 5520 8841 2305</div>
  <div class="divider" style="top:333px"></div>

  <svg class="contact-icon" style="top:342px" viewBox="0 0 36 36" aria-hidden="true">
    <circle cx="18" cy="18" r="18" fill="#fff"/>
    <circle cx="18" cy="18" r="9" fill="#9a9a9c"/>
    <ellipse cx="18" cy="18" rx="4" ry="9" fill="none" stroke="#fff" stroke-width="1"/>
    <path d="M9 18 H27 M11 13 H25 M11 23 H25" stroke="#fff" stroke-width="1"/>
  </svg>
  <div class="contact-text" style="top:350px">www.websitename.com</div>

  <div class="brand-name">Corvale Spine &amp; Joint</div>
</section>

</body>
</html>
```